Psychology practice - information brochure/flyer - half A4 page folded (4 sides)

We need a brochure/flyer to market our psychology service to GPs (Doctors). We need to demonstrate to the doctors that we are the right choice for their patients, and that we cover a large range of services so all of their patients needs are met. We will demonstrate this by listing our range of services and our team of psychologists. We have two locations in Sydney and offer high end services. I've attached our company logo but we remain flexible regarding the style of the brochures. I will provide more details (services, locations & psychologist credentials) once our preferred brochure design has been selected.

```html
<!DOCTYPE html>
<html lang="en">
<head>
<meta charset="utf-8">
<title>Clear Mind Clinical Psychology – Brochure Cover</title>
<link rel="stylesheet" href="https://fonts.googleapis.com/css2?family=Nunito+Sans:wght@300&display=swap">
<style>
  :root {
    --backdrop: #c4c4c6;
    --cover: #6e6d6b;
    --accent: #e8c21a;
    --logo-text: #ffffff;
    --photo-a1: #8a8580;
    --photo-a2: #cfcac2;
    --photo-b1: #5d6470;
    --photo-b2: #c9c1b3;
    --photo-c1: #dfe6e2;
    --photo-c2: #b4aa9b;
  }
  * { margin: 0; padding: 0; box-sizing: border-box; }
  html, body {
    width: 1200px;
    height: 900px;
    overflow: hidden;
    background: var(--backdrop);
  }
  .cover {
    position: absolute;
    left: 310px;
    top: 40px;
    width: 581px;
    height: 820px;
    background: var(--cover);
    font-family: "Nunito Sans", sans-serif;
    font-weight: 300;
  }
  .photo {
    position: absolute;
    width: 190px;
    height: 193px;
  }
  .photo--consultation {
    left: 0; top: 216px;
    background: linear-gradient(135deg, var(--photo-a1), var(--photo-a2));
  }
  .photo--session {
    left: 0; top: 409px;
    background: linear-gradient(135deg, var(--photo-b1), var(--photo-b2));
  }
  .photo--support {
    left: 190px; top: 409px;
    width: 194px;
    background: linear-gradient(135deg, var(--photo-c1), var(--photo-c2));
  }
  .brand {
    position: absolute;
    left: 232px;
    top: 292px;
    display: flex;
    align-items: center;
    gap: 12px;
    color: var(--logo-text);
  }
  .brand__mark {
    width: 26px;
    height: 26px;
    background: var(--accent);
    flex: none;
  }
  .brand__name {
    line-height: 1.05;
    letter-spacing: -0.3px;
  }
  .brand__name-main { display: block; font-size: 37px; }
  .brand__name-sub { display: block; font-size: 28px; }
  .tagline {
    position: absolute;
    left: 39px;
    top: 638px;
    color: var(--accent);
    font-size: 23px;
    line-height: 31px;
  }
</style>
</head>
<body>
  <main class="cover">
    <div class="photo photo--consultation" role="img" aria-label="Photo of a smiling psychologist holding a clipboard with colleagues seated behind"></div>
    <div class="photo photo--session" role="img" aria-label="Photo of a distressed man with his head in his hands beside a counsellor"></div>
    <div class="photo photo--support" role="img" aria-label="Photo of two hands clasped in a supportive gesture"></div>

    <div class="brand">
      <span class="brand__mark" aria-hidden="true"></span>
      <h1 class="brand__name">
        <span class="brand__name-main">Clear Mind</span>
        <span class="brand__name-sub">Clinical Psychology</span>
      </h1>
    </div>

    <p class="tagline">Working together to achieve<br>a better quality of life</p>
  </main>
</body>
</html>
```